Career-focused learning application platform

We have a K-12 learning application platform designed for grades 6-12 that needs user interface improvements that provide a positive experience for all users (teachers and students). The learning platform provides career-focused math curriculum and career exploration resources. We would like to improve the user-interface with engaging design elements without taking away from the functionality and performance of the platform.

```html
<!DOCTYPE html>
<html lang="en">
<head>
<meta charset="utf-8">
<title>Pathwell – Career Readiness For All Students</title>
<link href="https://fonts.googleapis.com/css2?family=Open+Sans:ital,wght@0,400;0,600;0,700;1,400&display=swap" rel="stylesheet">
<style>
:root{
  --orange:#f26a2e;
  --amber:#f7921e;
  --navy:#0d4a72;
  --ink:#333;
  --muted:#666;
  --line:#d9d9d9;
  --soft:#f2f2f2;
  --intro-bg:#fafafa;
  --white:#fff;
}
*{box-sizing:border-box;margin:0;padding:0}
html,body{width:1200px;height:3289px;overflow:hidden}
body{font-family:"Open Sans",Arial,sans-serif;color:var(--ink);background:var(--white);position:relative}
a{color:inherit}
section,header,footer{position:absolute;left:0;width:1200px}

.site-header{top:0;height:79px}
.brand{position:absolute;left:122px;top:24px;display:flex;align-items:center;gap:8px;font-size:24px;color:#555}
.brand-mark{width:22px;height:22px;border-radius:50%;background:var(--orange)}
.main-nav{position:absolute;right:123px;top:22px;display:flex;align-items:center;gap:14px;font-size:14.5px;color:#333}
.btn{display:inline-block;background:var(--orange);color:var(--white);border-radius:6px;font-weight:600;text-decoration:none}
.main-nav .btn{padding:8px 22px}

.hero{top:79px;height:328px;background:linear-gradient(90deg,#5a5f67 0%,#61666d 55%,#4f545b 100%)}
.hero-photo{position:absolute;right:0;top:0;width:440px;height:328px;background:linear-gradient(180deg,#6a6e73 0%,#4a4e54 60%,#6b3434 100%)}
.hero-copy{position:absolute;left:122px;top:40px;width:400px;color:var(--white)}
.hero-copy h1{font-weight:400;font-size:39px;line-height:1.06}
.hero-copy p{font-size:14.5px;line-height:23px;margin-top:12px}
.hero-copy .btn{margin-top:30px;padding:8px 17px;font-size:15px}

.intro{top:407px;height:672px;background:linear-gradient(180deg,var(--intro-bg) 0%,var(--white) 100%);text-align:center}
.intro h2{font-weight:400;font-size:29px;margin-top:80px;color:#333}
.intro p{width:630px;margin:14px auto 0;font-size:14px;line-height:24.5px;color:#555;letter-spacing:-0.1px}
.video-card{position:absolute;left:283px;top:277px;width:634px;height:316px;border-radius:12px;background:linear-gradient(135deg,#3a4550,#1f2a33 60%,#3a2c20);box-shadow:0 18px 36px rgba(0,0,0,.22)}
.play{position:absolute;left:272px;top:113px;width:90px;height:90px;border-radius:50%;background:rgba(255,255,255,.85)}
.play svg{position:absolute;left:30px;top:26px}

.features{top:1079px;height:395px;text-align:center}
.section-title{font-weight:600;font-size:29px;color:#333}
.features .section-title{margin-top:42px}
.feature-list{position:absolute;top:130px;left:0;width:1200px}
.feature{position:absolute;width:300px;margin-left:-150px}
.feature-icon{width:120px;height:120px;margin:0 auto;border-radius:50%;background:var(--white);box-shadow:0 4px 14px rgba(0,0,0,.12);position:relative}
.feature-icon span{position:absolute;left:38px;top:38px;width:44px;height:44px;border-radius:8px}
.feature h3{font-weight:400;font-size:17.5px;margin-top:18px}
.feature p{font-size:14.5px;line-height:23px;color:#555;margin-top:1px}

.testimonials{top:1474px;height:380px;background:var(--soft);text-align:center}
.testimonials .section-title{margin-top:36px}
.quote-card{position:absolute;left:342px;top:110px;width:517px;height:162px;background:var(--white);border-radius:18px;box-shadow:0 4px 10px rgba(0,0,0,.1);text-align:left;padding:20px 28px 0 36px}
.quote-card blockquote{font-style:italic;font-size:15.5px;line-height:25px;color:#444}
.author{display:flex;align-items:center;gap:12px;margin-top:16px}
.avatar{width:60px;height:60px;border-radius:50%;background:#3d3d3d}
.author strong{display:block;font-weight:400;font-size:16px;color:#222}
.author small{font-size:12.5px;color:#888}
.dots{position:absolute;top:323px;left:0;width:100%;display:flex;justify-content:center;gap:10px}
.dots i{width:13px;height:13px;border-radius:50%;background:var(--navy);border:1.5px solid var(--navy)}
.dots i.off{background:transparent}

.resources{top:1854px;height:506px;text-align:center}
.resources .section-title{margin-top:42px}
.resource-card{position:absolute;top:126px;width:309px;height:285px;border:1px solid var(--line);border-radius:6px;overflow:hidden;box-shadow:0 2px 4px rgba(0,0,0,.06)}
.resource-thumb{height:174px}
.resource-card h3{font-weight:400;font-size:22px;line-height:26px;margin-top:14px;color:#333}
.resource-card a{display:block;margin-top:7px;font-size:14.5px;color:var(--navy)}
.more-link{position:absolute;top:436px;left:0;width:100%;font-size:18px}
.more-link a{color:var(--navy)}

.subscribe{top:2360px;height:560px;background:var(--amber);text-align:center}
.subscribe h2{font-weight:700;font-size:34px;color:var(--navy);margin-top:40px}
.form-card{position:absolute;left:365px;top:114px;width:470px;height:360px;background:var(--white);border-radius:16px;text-align:left;padding:38px 37px 0}
.field{margin-bottom:22px}
.field label{display:block;font-size:12.5px;color:#333;margin-bottom:5px}
.field div{height:33px;border:1px solid #ccc;border-radius:6px;padding:8px 14px;font-size:12px;color:#999;box-shadow:0 2px 3px rgba(0,0,0,.06)}
.form-card .btn{background:var(--amber);padding:7px 26px;font-size:14px;margin-top:3px}

.site-footer{top:2920px;height:369px;text-align:center;color:#333}
.footer-brand{display:flex;justify-content:center;align-items:center;gap:12px;margin-top:66px;font-size:42px;color:#555}
.footer-brand .brand-mark{width:46px;height:46px}
.address{font-size:17px;margin-top:12px}
.contact-line{display:flex;justify-content:center;align-items:center;gap:8px;font-size:14.5px;margin-top:10px}
.socials{display:flex;justify-content:center;gap:10px;margin-top:12px}
.socials span{width:31px;height:31px;border-radius:50%;background:#8a8a8a}
.copyright{font-size:15px;margin-top:36px;color:#555}
.copyright a{color:var(--amber);margin-left:14px}
</style>
</head>
<body>

<header class="site-header">
  <div class="brand"><span class="brand-mark"></span>Pathwell</div>
  <nav class="main-nav">
    <span>Products &amp; Services</span><span>Resource Center</span><span>News &amp; Blog</span><span>About</span><span>Contact</span><span>Login</span>
    <a class="btn" href="#">Sign Up</a>
  </nav>
</header>

<section class="hero">
  <div class="hero-photo" role="img" aria-label="Photo of a student with a cap and red backpack looking ahead"></div>
  <div class="hero-copy">
    <h1>Career Readiness<br>For All Students</h1>
    <p>Suspendisse ac nulla eros. Vestibulum elementum placerat erat ac maximus. Aliquam quis nisi quis arcu dapibus ornare. Donec vel ex urna. Ut in odio ultricies mauris fringilla placerat commodo in augue.</p>
    <a class="btn" href="#">Get Started</a>
  </div>
</section>

<section class="intro">
  <h2>When they can see it, they can be it.</h2>
  <p>Every student can do great things when given a opportunity to learn and discover the future paths through career exploration.By connecting learning to careers student can discover opportunities and create their path to success. PATHWELL is a value Partner in the education industry working to provide evidence-based, career readiness solutions for all students.</p>
  <div class="video-card" role="img" aria-label="Video still of students building a robotics project together">
    <div class="play"><svg width="34" height="38" viewBox="0 0 34 38"><path d="M4 3 L31 19 L4 35 Z" fill="#111" stroke="#111" stroke-width="4" stroke-linejoin="round"/></svg></div>
  </div>
</section>

<section class="features">
  <h2 class="section-title">Features</h2>
  <div class="feature-list">
    <div class="feature" style="left:277px">
      <div class="feature-icon"><span role="img" aria-label="Career learning icon" style="background:#1d4f86"></span></div>
      <h3>Career Based Learning</h3>
      <p>Suspendisse ac nulla eros. Vestibulum elementum placerat erat ac maximus</p>
    </div>
    <div class="feature" style="left:600px">
      <div class="feature-icon"><span role="img" aria-label="Certificate icon" style="background:#f0922b"></span></div>
      <h3>Professional Development</h3>
      <p>Suspendisse ac nulla eros. Vestibulum elementum placerat erat ac maximus</p>
    </div>
    <div class="feature" style="left:923px">
      <div class="feature-icon"><span role="img" aria-label="Connected brain icon" style="background:#17807f;border-radius:50%"></span></div>
      <h3>Personalized Solutions</h3>
      <p>Suspendisse ac nulla eros. Vestibulum elementum placerat erat ac maximus</p>
    </div>
  </div>
</section>

<section class="testimonials">
  <h2 class="section-title">What teachers are saying about us</h2>
  <div class="quote-card">
    <blockquote>Never in my 20 years of educational experience have my students ever experienced such in-depth career-focused math problems.</blockquote>
    <div class="author">
      <div class="avatar" role="img" aria-label="Portrait of the teacher"></div>
      <div><strong>John Doe</strong><small>Teacher &amp; Trainer</small></div>
    </div>
  </div>
  <div class="dots"><i class="off"></i><i></i><i></i></div>
</section>

<section class="resources">
  <h2 class="section-title">Resource Center</h2>
  <article class="resource-card" style="left:122px">
    <div class="resource-thumb" role="img" aria-label="Video cover about investing in student pathways with a tablet chart" style="background:linear-gradient(90deg,#d8323a 0 27%,#2d4b6b 27%,#7f9fbf 100%)"></div>
    <h3>Investing in Student<br>Pathways</h3>
    <a href="#">View Resource</a>
  </article>
  <article class="resource-card" style="left:445px">
    <div class="resource-thumb" role="img" aria-label="Report cover showing students working in a classroom" style="background:linear-gradient(180deg,#fff 0 22%,#8a8f96 22%,#c9ccd0 68%,#fff 68%)"></div>
    <h3>Investing in Student<br>Pathways</h3>
    <a href="#">View Resource</a>
  </article>
  <article class="resource-card" style="left:768px">
    <div class="resource-thumb" role="img" aria-label="Students collaborating in a library with an orange diagonal band" style="background:linear-gradient(115deg,#ee7a22 0 38%,#a79a94 38%,#d4c6c0 100%)"></div>
    <h3>Investing in Student<br>Pathways</h3>
    <a href="#">View Resource</a>
  </article>
  <div class="more-link"><a href="#">View Resource</a></div>
</section>

<section class="subscribe">
  <h2>Subscribe For Updates</h2>
  <form class="form-card">
    <div class="field"><label>First Name</label><div>First name</div></div>
    <div class="field"><label>Last Name</label><div>Last name</div></div>
    <div class="field"><label>Email Address</label><div>Email@email.com</div></div>
    <span class="btn">Subscrib</span>
  </form>
</section>

<footer class="site-footer">
  <div class="footer-brand"><span class="brand-mark"></span>Pathwell</div>
  <p class="address">48 Harbor Lane, Suite 10, Millbrook, OR 97012</p>
  <p class="contact-line">
    <svg width="24" height="18" viewBox="0 0 24 18"><rect x="1.5" y="1.5" width="21" height="15" rx="2" fill="none" stroke="#333" stroke-width="2"/><path d="M2 3 L12 10 L22 3" fill="none" stroke="#333" stroke-width="2"/></svg>
    hello@pathwell-learn.com
  </p>
  <p class="contact-line">
    <svg width="26" height="26" viewBox="0 0 24 24"><path d="M6.6 10.8a15 15 0 0 0 6.6 6.6l2.2-2.2a1 1 0 0 1 1-.25 11 11 0 0 0 3.6.6 1 1 0 0 1 1 1V20a1 1 0 0 1-1 1A17 17 0 0 1 3 4a1 1 0 0 1 1-1h3.5a1 1 0 0 1 1 1 11 11 0 0 0 .6 3.6 1 1 0 0 1-.25 1z" fill="none" stroke="#333" stroke-width="1.8"/></svg>
    555.210.0147
  </p>
  <div class="socials"><span></span><span></span><span></span><span></span></div>
  <p class="copyright">Copyrights Reserved @ 2021 PATHWELL <a href="#">Privacy Policy</a></p>
</footer>

</body>
</html>
```